Marketing materials for computer support company
trifolds, sign, and magnet
Thank you everyone for your submissions! They were all wonderful.
draft #18 is great - we will spend some time to more carefully review it and give some specific feedback later today. Thanks again
regarding draft #13 and draft #12, these are what we are looking for. The dark photo with the people we would like to go though. We are a small company and don't want to misrepresent that.
We are would use draft #12 for commercial services and draft #13 for residential. Is there anything that could be done to make them slightly different from each other inside though? If not, I'm sure we will find some content to fit - but if someone took one of each brochure, I don't want them to look identical other than the front and color. Maybe even just a different image in the middle of draft #12 where the laptop/wrench image is? Anyway, awesome work!
regarding draft #11, I prefer this to draft #5. Just something doesn't quite fit for me - I'll try to come up with something more specific. Thanks though - this is currently our 2nd favorite
regarding draft #10, I hadn't thought about it before, but I love how one brochure uses mostly blue, and the other uses mostly orange. I also like the flow of both of these. I can't tell if they are tri-fold though. But if you were wondering if we'd like the idea - we do!
-Wade
Also, if it helps, you can checkout what we liked / didn't like in our ongoing stationery / business card content!
Our contest link is: http://www.quintaloft.net/contests/business-card-template-company-stationery
so I will try to be more specific to assist until the unveil it - but bear with me, this is not my area :-) So blue and orange are preferable. Less gradients are better. Curves and circles that flow across the entire front or back for the residential tri-fold connecting the content areas is preferable. Same idea, but with straight angled boxes seems to be what I like on the business tri-fold. Pictures seem more important on the business one (based on existing designs that we have seen), residential can use illustrations in place of pictures. That's what I've got for now!
I just noticed this project is listed as "veiled" even though I did not choose to do so, so I apologize if you can not see the comparisons I am making between each others designs. I will contact support to fix this.
regarding draft #1, thank you for the submission. While I will make some remarks about what I would like to see in the layout, this set of documents is very much along the lines of what I am looking for. The 8.5x11 represents the content of the tri-fold and the magnet has room for a 1" x 3" label. I also like the use of blue! There is something plain about the actual layout though, in comparison to the angles used in draft #4 business tri-fold or curves of draft #4 residential. Thanks again for the submission!
regarding draft #2, I really like the use of our colors and thank you for the submission! I would like more photos as opposed to graphics such as the "help / mouse" or "laptop with stethoscope". I felt the overall feel was very busy and took up a lot of space without providing much room for content. I did like the use of our logo, but I'm ok with it taking up less room in exchange for a really clean look.
regarding draft #3, I like the nerdy magnet guy, but needs room for a 1"x3" thermal label and more room for our name / contact info
regarding draft #4, I like the look of the business tri-fold more than that of the residential. The graphic for the back especially. I think the colors on the residential need to be brighter and more playful. I think the idea of the business tri-fold having more straight lines and sharp angles, while the residential has more curves is great. Just the colors and overall look don't appeal to me. While neither of the magnets would fit a 1x3 label I LOVE how simple the magnet with our logo cutout looks - great idea!

```html
<!DOCTYPE html>
<html lang="en">
<head>
<meta charset="utf-8">
<title>Brightline Computer Support – Tri-fold Brochure</title>
<link href="https://fonts.googleapis.com/css2?family=Roboto:ital,wght@0,400;0,700;0,900;1,700&display=swap" rel="stylesheet">
<style>
:root{
  --blue:#1d5fa8;
  --blue-dark:#123f78;
  --blue-light:#3f8fd6;
  --orange:#f28a1e;
  --orange-dark:#d9640f;
  --orange-light:#ffb347;
  --ink:#333;
  --muted:#666;
  --paper:#fff;
  --stage:#e9e6e1;
}
*{box-sizing:border-box;margin:0;padding:0}
html,body{width:1200px;height:1104px;overflow:hidden;background:var(--stage);font-family:"Roboto",Arial,sans-serif;color:var(--ink)}
.spread{position:absolute;left:0;width:1200px;height:530px;background:var(--paper);display:flex;overflow:hidden}
.spread--outside{top:0}
.spread--inside{top:574px}
.panel{position:relative;width:400px;height:530px;overflow:hidden;border-right:1px solid #e3e3e3}
.panel:last-child{border-right:none}
.swoosh{position:absolute;left:0;width:400px}
.photo{position:absolute}
.photo--blue{background:linear-gradient(135deg,#dfe7ef,#7f9bb8)}
.photo--warm{background:linear-gradient(135deg,#f1d3b3,#9a7a62)}
.photo--office{background:linear-gradient(135deg,#cfd9e3,#6b7f93)}

/* outside – left */
.mission{position:absolute;left:28px;top:24px;width:240px;color:var(--orange-dark);font-weight:700;font-style:italic;font-size:14px;line-height:1.35}
.mission .mark{position:absolute;left:-22px;top:-14px;font-size:46px;color:var(--orange)}
.covered-tab{position:absolute;left:0;top:206px;width:250px;height:30px;background:var(--blue);color:#fff;font-weight:700;font-size:15px;line-height:30px;padding-left:34px;border-radius:0 15px 15px 0}
.service-list{position:absolute;left:34px;top:250px;list-style:none}
.service-list li{font-size:13px;font-weight:700;color:var(--blue-dark);margin-bottom:9px;display:flex;align-items:center;gap:8px}
.service-list svg{width:14px;height:14px}

/* outside – middle */
.hours-box{position:absolute;left:0;top:0;width:400px;height:200px;background:linear-gradient(180deg,var(--orange-light),var(--orange))}
.hours-box h3{position:absolute;left:200px;top:14px;font-size:14px;color:#fff;letter-spacing:1px}
.hours-box .hours{position:absolute;left:200px;top:36px;color:#fff;font-size:11.5px;line-height:1.45;font-weight:700}
.hours-box .invite{position:absolute;left:200px;top:140px;width:180px;color:#fff;font-size:10px;line-height:1.3}
.hours-photo{left:0;top:0;width:180px;height:200px}
.addresses{position:absolute;left:120px;top:300px;font-size:11px;line-height:1.45;color:var(--ink)}
.addresses b{display:block;color:var(--blue-dark);font-size:11.5px;margin-top:8px}
.addresses .phone{margin-top:12px}
.pin{position:absolute;left:80px;top:304px;width:26px;height:26px}

/* outside – right (cover) */
.cover-photo{left:0;top:0;width:400px;height:210px}
.brand{position:absolute;left:100px;top:240px;display:flex;align-items:center;gap:10px}
.brand .dot{width:26px;height:26px;border-radius:50%;background:var(--blue)}
.brand .name{font-size:22px;font-weight:700;color:var(--blue)}
.cover-url{position:absolute;left:0;bottom:22px;width:400px;text-align:center;color:#fff;font-size:14px;font-weight:700}

/* inside */
.url-bar{position:absolute;left:0;top:0;width:400px;height:34px;background:linear-gradient(90deg,var(--orange),var(--orange-light));color:#fff;font-weight:700;font-size:15px;line-height:34px;padding-left:24px}
.pill{position:absolute;top:50px;left:24px;height:24px;padding:0 16px;border-radius:12px;background:var(--blue);color:#fff;font-weight:900;font-size:13px;line-height:24px;letter-spacing:.5px}
.pill--orange{background:var(--orange)}
.body{position:absolute;left:24px;width:352px;font-size:10px;line-height:1.42;color:var(--muted)}
.body p{margin-bottom:8px}
.body h4{color:var(--blue-dark);font-size:12px;margin:6px 0 3px}
.body h4.orange{color:var(--orange-dark)}
.about-photo{left:0;top:380px;width:400px;height:150px}
.svc-lead{font-size:13px!important;color:var(--blue-dark)!important;font-weight:700}
.svc-item{position:absolute;left:24px;width:352px;display:flex;gap:12px;font-size:10px;line-height:1.4;color:var(--muted)}
.svc-item .thumb{flex:0 0 70px;height:56px;border-radius:4px}
.svc-item b{display:block;color:var(--blue-dark);font-size:11px;margin-bottom:2px}
.apart-bar{position:absolute;left:0;top:0;width:400px;height:34px;background:var(--blue);color:#fff;font-weight:700;font-size:13px;line-height:34px;padding-left:24px}
.callout{position:absolute;left:24px;top:440px;width:190px;color:var(--orange-dark);font-weight:700;font-size:12px;line-height:1.35}
.callout-photo{left:230px;top:400px;width:170px;height:130px;border-radius:85px 0 0 0}
</style>
</head>
<body>

<!-- OUTSIDE -->
<section class="spread spread--outside">
  <div class="panel panel--mission">
    <p class="mission"><span class="mark">“</span>Our goal is to make sure each client gets the attention they deserve by providing prompt, reliable and skilled technical support as well as impartial advice and strategies on dealing with business technology.</p>
    <div class="photo photo--blue" style="left:280px;top:20px;width:110px;height:150px" role="img" aria-label="Photo of a smiling technician"></div>
    <svg class="swoosh" style="top:170px" height="40" viewBox="0 0 400 40"><path d="M0 30 Q200 -5 400 15 L400 22 Q200 5 0 40Z" fill="var(--orange)"/></svg>
    <div class="covered-tab">We've Got You Covered!</div>
    <ul class="service-list">
      <li><svg viewBox="0 0 14 14"><path d="M2 7l3 3 7-7" stroke="var(--orange)" stroke-width="2.5" fill="none"/></svg>Personal Computer Repair</li>
      <li><svg viewBox="0 0 14 14"><path d="M2 7l3 3 7-7" stroke="var(--orange)" stroke-width="2.5" fill="none"/></svg>On-Site Commercial Support</li>
      <li><svg viewBox="0 0 14 14"><path d="M2 7l3 3 7-7" stroke="var(--orange)" stroke-width="2.5" fill="none"/></svg>Remote Maintenance Plans</li>
      <li><svg viewBox="0 0 14 14"><path d="M2 7l3 3 7-7" stroke="var(--orange)" stroke-width="2.5" fill="none"/></svg>Convenient Store Location</li>
      <li><svg viewBox="0 0 14 14"><path d="M2 7l3 3 7-7" stroke="var(--orange)" stroke-width="2.5" fill="none"/></svg>Certified &amp; Insured</li>
    </ul>
    <div class="photo photo--office" style="left:0;top:400px;width:400px;height:130px" role="img" aria-label="Photo of a businessman presenting beside a laptop"></div>
    <svg class="swoosh" style="top:385px" height="40" viewBox="0 0 400 40"><path d="M0 10 Q200 40 400 5 L400 0 L0 0Z" fill="#fff"/><path d="M0 12 Q200 42 400 7 L400 14 Q200 48 0 20Z" fill="var(--blue)"/></svg>
  </div>

  <div class="panel panel--contact">
    <div class="hours-box">
      <div class="photo photo--warm hours-photo" role="img" aria-label="Photo of a computer workstation"></div>
      <h3>STORE HOURS</h3>
      <p class="hours">Hours of Operation<br>Mon 9:30am - 6:00pm<br>Tue 9:30am - 6:00pm<br>Wed 9:30am - 6:00pm<br>Thu 9:30am - 6:00pm<br>Fri 9:30am - 5:00pm</p>
      <p class="invite">Want a tailored plan for your home or office? Call us today or stop by for a free consultation.</p>
    </div>
    <svg class="swoosh" style="top:190px" height="40" viewBox="0 0 400 40"><path d="M0 10 Q200 40 400 0 L400 40 L0 40Z" fill="#fff"/><path d="M0 8 Q200 38 400 -2 L400 6 Q200 46 0 16Z" fill="var(--blue)"/></svg>
    <svg class="pin" viewBox="0 0 26 26"><path d="M13 2a8 8 0 0 0-8 8c0 6 8 14 8 14s8-8 8-14a8 8 0 0 0-8-8z" fill="var(--orange)"/><circle cx="13" cy="10" r="3" fill="#fff"/></svg>
    <div class="addresses">
      <b>STORE ADDRESS</b>120 Main St, Harbor, WI 54321
      <b>MAILING ADDRESS</b>PO Box 118, Harbor, WI 54321
      <div class="phone">Phone: 555-010-4410<br>Fax: 555-010-4411</div>
    </div>
    <svg class="swoosh" style="top:440px" height="90" viewBox="0 0 400 90"><path d="M0 40 Q200 0 400 30 L400 90 L0 90Z" fill="var(--orange)"/><path d="M0 30 Q200 -10 400 20 L400 30 Q200 0 0 40Z" fill="var(--blue)"/></svg>
  </div>

  <div class="panel panel--cover">
    <div class="photo photo--office cover-photo" role="img" aria-label="Photo of a technician in glasses and a suit"></div>
    <svg class="swoosh" style="top:180px" height="50" viewBox="0 0 400 50"><path d="M0 30 Q200 0 400 25 L400 50 L0 50Z" fill="#fff"/><path d="M0 28 Q200 -4 400 22 L400 30 Q200 6 0 38Z" fill="var(--orange)"/></svg>
    <div class="brand"><span class="dot"></span><span class="name">Brightline Computer Support</span></div>
    <svg class="swoosh" style="top:330px" height="200" viewBox="0 0 400 200"><path d="M0 80 Q200 0 400 50 L400 200 L0 200Z" fill="var(--orange)"/><path d="M0 70 Q200 -12 400 38 L400 50 Q200 0 0 80Z" fill="var(--blue)"/></svg>
    <div class="cover-url">brightlinetechhelp.com</div>
  </div>
</section>

<!-- INSIDE -->
<section class="spread spread--inside">
  <div class="panel panel--about">
    <div class="url-bar">brightlinetechhelp.com</div>
    <div class="pill">ABOUT US</div>
    <div class="body" style="top:86px">
      <p>Located in Harbor, Brightline Computer Support has served local homes and businesses since 2004. Our technicians hold industry certifications and bring years of hands-on experience to every repair, upgrade and installation we perform for our clients.</p>
      <p>We believe technology should work for you, not against you. That is why we explain every option in plain language, give honest recommendations and never push services you do not need.</p>
      <p>From a single laptop to a growing office network, our small team treats each job with the same care. We keep our prices fair, our turnaround fast and our doors open six days a week.</p>
      <p>Stop by our store or schedule a visit and see why so many neighbors trust us.</p>
    </div>
    <div class="photo photo--warm about-photo" role="img" aria-label="Photo of the support team at work"></div>
  </div>

  <div class="panel panel--services">
    <div class="url-bar" style="background:linear-gradient(90deg,var(--orange-light),var(--orange))"></div>
    <div class="pill pill--orange">SERVICES</div>
    <div class="body" style="top:84px">
      <p class="svc-lead">Computer, Network, &amp; Phone Support… now in Harbor</p>
      <p>Our consultants and technicians design, install and maintain systems that fit your budget and keep your team productive every single day.</p>
    </div>
    <div class="svc-item" style="top:170px"><div class="thumb photo--blue" role="img" aria-label="Illustration of a consultant"></div><div><b>CONSULTING</b>Not sure where to start? We review your equipment and goals, then map out a clear plan.</div></div>
    <div class="svc-item" style="top:250px"><div class="thumb photo--office" role="img" aria-label="Illustration of network security"></div><div><b>NETWORK SECURITY</b>Firewalls, backups and monitoring that keep your data safe from threats and loss.</div></div>
    <div class="svc-item" style="top:330px"><div class="thumb photo--warm" role="img" aria-label="Illustration of a desk phone"></div><div><b>VOIP PHONE SYSTEMS</b>Modern phone systems that cut costs and move with your business as it grows.</div></div>
    <svg class="swoosh" style="top:440px" height="90" viewBox="0 0 400 90"><path d="M0 50 Q200 10 400 40 L400 90 L0 90Z" fill="var(--blue)"/><path d="M0 40 Q200 0 400 30 L400 40 Q200 10 0 50Z" fill="var(--orange)"/></svg>
  </div>

  <div class="panel panel--apart">
    <div class="apart-bar">What sets us apart from the rest?</div>
    <div class="body" style="top:48px">
      <h4>In Store Repair</h4>
      <p>Bring your desktop or laptop to our store for diagnostics, virus removal, upgrades and data recovery, usually finished within two business days.</p>
      <h4>In Home or In Office Computer Support</h4>
      <p>Our technicians come to you to set up new equipment, fix wireless problems and train your family or staff on the tools they use.</p>
      <h4>Remote Commercial Maintenance</h4>
      <p>Monthly plans keep your office running with updates, backups and remote fixes, often before you notice a problem.</p>
    </div>
    <p class="callout">Please call Brightline Tech at 555-010-4410 with any questions!</p>
    <div class="photo photo--warm callout-photo" role="img" aria-label="Photo of a support representative with a headset"></div>
  </div>
</section>

</body>
</html>
```